Leaflets
We supply stone and solid surfaces to the trade and project manage its installation
Project: Leaflets
Leaflets - Construction
Creative Brief
Construction
Architects, Interior designers, property developers, kitchen and bathroom designers, shopfitters Our offer is mainly business to business. Our branding and images are corporate and our content (wording) is more casual (which is what makes us different from the competition)
A leaflet with our branding, logos and fonts to be used as an introduction to our clients mainly targeted trough site visits and by posting samples. Images and branding available on request.

```html
<!DOCTYPE html>
<html lang="en">
<head>
<meta charset="utf-8">
<title>Trelvax – Stone Services Leaflet</title>
<link href="https://fonts.googleapis.com/css2?family=Mulish:wght@600;700&display=swap" rel="stylesheet">
<style>
  :root {
    --paper: #ffffff;
    --ink: #3d3d3f;
    --brand-green: #8cc63f;
    --brand-purple: #6b2c91;
    --brand-grey: #a7a9ac;
    --divider: #ffffff;
  }
  html, body {
    margin: 0;
    padding: 0;
    overflow: hidden;
    background: var(--paper);
  }
  .leaflet {
    position: relative;
    width: 1200px;
    height: 932px;
    background: var(--paper);
    overflow: hidden;
    font-family: "Mulish", "Helvetica Neue", Arial, sans-serif;
  }
  .brand-name {
    position: absolute;
    left: 106px;
    top: 230px;
    margin: 0;
    font-family: "Mulish", Arial, sans-serif;
    font-weight: 700;
    font-size: 78px;
    letter-spacing: 1px;
    color: var(--brand-green);
  }
  .intro {
    position: absolute;
    left: 131px;
    top: 584px;
    width: 446px;
    margin: 0;
    font-size: 16.4px;
    line-height: 27.4px;
    font-weight: 700;
    color: var(--ink);
    text-align: justify;
  }
  .colour-strip {
    position: absolute;
    left: 599px;
    top: 0;
    width: 63px;
    height: 932px;
    display: flex;
    flex-direction: column;
  }
  .colour-strip .band-purple { height: 303px; background: var(--brand-purple); }
  .colour-strip .band-grey { height: 316px; background: var(--brand-grey); }
  .colour-strip .band-green { flex: 1; background: var(--brand-green); }
  .gallery {
    position: absolute;
    left: 662px;
    top: 0;
    width: 538px;
    height: 932px;
    display: flex;
    flex-direction: column;
    gap: 5px;
    background: var(--divider);
  }
  .photo { width: 100%; }
  .photo-worktop {
    height: 374px;
    background: linear-gradient(160deg, #e9ecea 0%, #c9cfc9 35%, #6d5a4c 60%, #8b7867 80%, #d9d6d0 100%);
  }
  .photo-interior {
    height: 245px;
    background: linear-gradient(180deg, #d8dbda 0%, #9ea3a3 35%, #4a4d50 60%, #b6b4ae 85%, #e2ded6 100%);
  }
  .photo-kitchen {
    flex: 1;
    background: linear-gradient(170deg, #cfc7bb 0%, #b9ae9f 40%, #e6dfd4 70%, #f3efe8 100%);
  }
</style>
</head>
<body>
  <main class="leaflet">
    <h1 class="brand-name">Trelvax</h1>

    <p class="intro">We share ten years' experience working in the stone industry; we know how time-consuming sourcing high quality products can be, not to mention the leg work that goes into finding experienced project managers and expert craftspeople to carry out the work. So what we've come up with is a complete service: you tell us what you need, we source the stone, put together the team, oversee the job and follow up with you afterwards to make sure everything is perfect. It sounds easy and straight-forward – and it is, but very few companies offer such a comprehensive package.</p>

    <div class="colour-strip" aria-hidden="true">
      <div class="band-purple"></div>
      <div class="band-grey"></div>
      <div class="band-green"></div>
    </div>

    <section class="gallery">
      <div class="photo photo-worktop" role="img" aria-label="Photo of a long brown stone kitchen worktop with white dishes in a bright glass-walled room"></div>
      <div class="photo photo-interior" role="img" aria-label="Photo of a modern open-plan kitchen interior with dark cabinets under a glazed roof"></div>
      <div class="photo photo-kitchen" role="img" aria-label="Photo of a cream curved kitchen island with sink and hob beneath a wicker pendant lamp"></div>
    </section>
  </main>
</body>
</html>
```